Business card design for Medical Practice Mgmt company
Ashfield Clinic Allies
Business card design for Medical Practice Mgmt company - Medical
Creative Brief
Professional
Monica Daltrey
VP of Operations
4170 E Holloway Ln # 210 Plano, TX 75041
mdaltrey@aca-mail.net
www.ashfieldclinicallies.net
jdovan jdovan
uploaded AI file
bluefern bluefern
Logo Ai file needed!

```html
<!DOCTYPE html>
<html lang="en">
<head>
<meta charset="utf-8">
<title>Ashfield Clinic Allies – Business Card</title>
<link href="https://fonts.googleapis.com/css2?family=Montserrat:wght@400;500;600&family=Roboto:wght@400;500&display=swap" rel="stylesheet">
<style>
  :root {
    --page-bg: #e9e9e7;
    --card-white: #ffffff;
    --card-black: #111111;
    --ink: #1f1f1f;
    --ink-soft: #6b6b6b;
    --rule: #c9c9c9;
    --accent-pink: #e6358f;
    --accent-orange: #f5921e;
    --accent-blue: #1f8fd1;
    --white: #ffffff;
  }
  * { box-sizing: border-box; margin: 0; padding: 0; }
  html, body { width: 1200px; height: 901px; overflow: hidden; }
  body {
    background: var(--page-bg);
    font-family: "Roboto", Arial, sans-serif;
    color: var(--ink);
    position: relative;
  }
  .card {
    position: absolute;
    top: 296px;
    width: 540px;
    height: 309px;
    border-radius: 14px;
    box-shadow: 0 6px 18px rgba(0,0,0,0.12);
    overflow: hidden;
  }
  .card--front { left: 40px; background: var(--card-white); }
  .card--back { left: 620px; background: var(--card-black); }

  .brand { position: absolute; display: flex; align-items: center; gap: 10px; }
  .brand__dot { width: 18px; height: 18px; border-radius: 50%; background: var(--accent-pink); flex: none; }
  .brand__name { font-family: "Montserrat", Arial, sans-serif; font-weight: 600; }

  .card--front .brand { left: 36px; top: 58px; }
  .card--front .brand__name { font-size: 22px; color: var(--ink); }
  .tagline {
    position: absolute; left: 64px; top: 92px;
    font-size: 7.5px; letter-spacing: 0.6px; text-transform: uppercase;
    color: var(--accent-blue);
  }

  .holder { position: absolute; right: 36px; top: 62px; text-align: right; }
  .holder__name { font-family: "Montserrat", Arial, sans-serif; font-size: 17px; font-weight: 500; color: var(--ink); }
  .holder__rule { height: 2px; width: 120px; background: var(--accent-pink); margin: 6px 0 0 auto; }

  .divider { position: absolute; left: 36px; top: 150px; width: 400px; height: 1px; background: var(--rule); }

  .address { position: absolute; left: 40px; top: 186px; font-size: 10px; line-height: 15px; color: var(--ink-soft); }

  .contacts { position: absolute; left: 196px; top: 176px; list-style: none; font-size: 10px; line-height: 15px; color: var(--ink-soft); }
  .contacts li { display: flex; align-items: center; gap: 6px; }
  .contacts svg { width: 9px; height: 9px; flex: none; }

  .web-pill {
    position: absolute; right: 0; bottom: 30px;
    background: var(--card-black); color: var(--white);
    font-size: 10px; padding: 5px 18px 5px 14px;
    border-radius: 12px 0 0 12px;
  }

  .card--back .brand { left: 50%; top: 50%; transform: translate(-50%, -50%); gap: 16px; }
  .card--back .brand__dot { width: 40px; height: 40px; }
  .card--back .brand__name { font-size: 28px; color: var(--white); white-space: nowrap; }
</style>
</head>
<body>
  <section class="card card--front" aria-label="Business card front">
    <div class="brand">
      <span class="brand__dot"></span>
      <span class="brand__name">Ashfield Clinic Allies</span>
    </div>
    <p class="tagline">Supporting independent practices across Texas</p>

    <div class="holder">
      <p class="holder__name">Monica Daltrey</p>
      <div class="holder__rule"></div>
    </div>

    <div class="divider"></div>

    <address class="address">
      4170 E Holloway Ln<br>
      # 210<br>
      Plano, TX 75041
    </address>

    <ul class="contacts">
      <li><svg viewBox="0 0 10 10"><rect width="10" height="10" rx="1.5" fill="var(--accent-orange)"/></svg>214-555-0182</li>
      <li><svg viewBox="0 0 10 10"><rect width="10" height="10" rx="1.5" fill="var(--accent-orange)"/></svg>214-555-0147</li>
      <li><svg viewBox="0 0 10 10"><rect width="10" height="10" rx="1.5" fill="var(--accent-orange)"/></svg>214-555-0193</li>
      <li><svg viewBox="0 0 10 10"><rect width="10" height="10" rx="1.5" fill="var(--accent-orange)"/></svg>mdaltrey@aca-mail.net</li>
    </ul>

    <p class="web-pill">www.ashfieldclinicallies.net</p>
  </section>

  <section class="card card--back" aria-label="Business card back">
    <div class="brand">
      <span class="brand__dot"></span>
      <span class="brand__name">Ashfield Clinic Allies</span>
    </div>
  </section>
</body>
</html>
```